Voltline Assemblies, Inc. Business Card

Voltline has three operating entities and I'm looking for a standard business card template that can be used for Voltline and the three operating entities that the logo just get swapped out, but has a very similar look and feel. Ultimately if someone had a business card from each, they assume the organizations are related because they all have the same look and feel.
Below are our websites and I will attached the logos for each entity:
https://www.voltlineassemblies.example/
https://www.brantoceramic.example/
https://www.omra-kfsd.example/
https://www.summitbreaker.example/

Target Market(s)

US Voltline

Industry/Entity Type

US Voltline

Contact Information for Business Card

Normal stuff

```html
<!DOCTYPE html>
<html lang="en">
<head>
<meta charset="utf-8">
<title>Voltline Assemblies, Inc. Business Card</title>
<link href="https://fonts.googleapis.com/css2?family=Montserrat:wght@700;800&family=Open+Sans:wght@400;600&display=swap" rel="stylesheet">
<style>
  :root {
    --stage: #2b2b2e;
    --navy: #1f2c6e;
    --indigo: #22226a;
    --blue-top: #2c5ea6;
    --blue-bottom: #23468d;
    --slate: #4f7589;
    --red: #c8202f;
    --white: #ffffff;
    --ink: #3b3b3b;
    --soft: #dfe6f2;
  }
  * { box-sizing: border-box; margin: 0; padding: 0; }
  html, body { width: 1200px; height: 900px; overflow: hidden; }
  body {
    background: var(--stage);
    font-family: "Open Sans", Arial, sans-serif;
    display: flex;
    flex-direction: column;
    align-items: center;
    justify-content: center;
    gap: 40px;
  }
  .card {
    width: 560px;
    height: 320px;
    position: relative;
    overflow: hidden;
    box-shadow: 0 10px 30px rgba(0,0,0,.45);
  }

  /* Front */
  .card-front { background: var(--white); }
  .card-front .swoosh { position: absolute; inset: 0; }
  .brand {
    position: absolute;
    left: 34px;
    top: 62px;
    display: flex;
    align-items: center;
    gap: 10px;
  }
  .brand-mark {
    width: 34px; height: 34px;
    border-radius: 50%;
    background: var(--navy);
  }
  .brand-name {
    font-family: "Montserrat", Arial, sans-serif;
    font-weight: 800;
    font-size: 30px;
    line-height: 1;
    color: var(--navy);
    text-transform: uppercase;
  }
  .brand-sub {
    position: absolute;
    left: 80px;
    top: 100px;
    font-family: "Montserrat", Arial, sans-serif;
    font-weight: 700;
    font-size: 11px;
    letter-spacing: 3px;
    color: var(--navy);
    text-transform: uppercase;
  }
  .front-url {
    position: absolute;
    left: 22px;
    bottom: 38px;
    color: var(--white);
    font-size: 12.5px;
  }
  .divider {
    position: absolute;
    left: 292px;
    top: 40px;
    width: 1.5px;
    height: 130px;
    background: var(--navy);
  }
  .contact {
    position: absolute;
    left: 308px;
    top: 40px;
    color: var(--ink);
    font-size: 13px;
    line-height: 1.5;
  }
  .person-name {
    font-family: "Montserrat", Arial, sans-serif;
    font-weight: 800;
    font-size: 18px;
    color: var(--navy);
    text-transform: uppercase;
    letter-spacing: .5px;
  }
  .person-title { color: var(--red); font-size: 14px; margin-bottom: 4px; }
  .contact-line { display: flex; align-items: center; gap: 6px; }
  .contact-line svg { width: 12px; height: 12px; flex: none; }

  /* Back */
  .card-back {
    display: grid;
    grid-template-columns: 1fr 1fr;
    grid-template-rows: 1fr 1fr;
  }
  .entity {
    display: flex;
    flex-direction: column;
    justify-content: center;
    padding: 0 26px;
    color: var(--white);
  }
  .entity-voltline { background: var(--navy); }
  .entity-branto { background: linear-gradient(180deg, var(--blue-top), var(--blue-bottom)); }
  .entity-omra { background: var(--indigo); }
  .entity-summit { background: var(--slate); }
  .entity-head { display: flex; align-items: center; gap: 8px; }
  .entity-mark { width: 18px; height: 18px; border-radius: 50%; background: var(--white); flex: none; }
  .entity-name {
    font-family: "Montserrat", Arial, sans-serif;
    font-weight: 800;
    font-size: 17px;
    text-transform: uppercase;
    line-height: 1.1;
  }
  .entity-tag { font-size: 8.5px; margin-top: 5px; color: var(--soft); }
  .entity-url { font-size: 12px; margin-top: 6px; }
</style>
</head>
<body>

<section class="card card-front" aria-label="Business card front">
  <svg class="swoosh" viewBox="0 0 560 320" preserveAspectRatio="none" aria-hidden="true">
    <path d="M0,178 C190,196 330,300 560,298 L560,320 L0,320 Z" fill="var(--navy)"/>
    <path d="M0,166 C195,184 335,288 560,286" fill="none" stroke="var(--red)" stroke-width="7"/>
    <path d="M0,160 C195,178 335,282 560,280" fill="none" stroke="var(--navy)" stroke-width="2"/>
  </svg>

  <div class="brand">
    <span class="brand-mark"></span>
    <span class="brand-name">Voltline</span>
  </div>
  <div class="brand-sub">Assemblies, Inc.</div>

  <div class="front-url">www.voltlineassemblies.example</div>

  <div class="divider"></div>
  <div class="contact">
    <div class="person-name">Dorian Halvek</div>
    <div class="person-title">President</div>
    <div>4820 Ridgeway Lane</div>
    <div>Suite 210, Fairhaven, AL 35900</div>
    <div class="contact-line">
      <svg viewBox="0 0 24 24" aria-hidden="true"><path fill="var(--red)" d="M6.6 10.8a15.1 15.1 0 0 0 6.6 6.6l2.2-2.2c.3-.3.7-.4 1-.2 1.1.4 2.3.6 3.6.6.6 0 1 .4 1 1V20c0 .6-.4 1-1 1A17 17 0 0 1 3 4c0-.6.4-1 1-1h3.5c.6 0 1 .4 1 1 0 1.3.2 2.5.6 3.6.1.3 0 .7-.2 1z"/></svg>
      <span>555 014 2273</span>
    </div>
    <div class="contact-line">
      <svg viewBox="0 0 24 24" aria-hidden="true"><path fill="var(--red)" d="M2 5h20v14H2z"/><path d="M2 5l10 8 10-8" fill="none" stroke="var(--white)" stroke-width="2"/></svg>
      <span>info@voltlineassemblies.example</span>
    </div>
  </div>
</section>

<section class="card card-back" aria-label="Business card back">
  <div class="entity entity-voltline">
    <div class="entity-head"><span class="entity-mark"></span><span class="entity-name">Voltline</span></div>
    <div class="entity-url">www.voltlineassemblies.example</div>
  </div>
  <div class="entity entity-branto">
    <div class="entity-head"><span class="entity-mark"></span><span class="entity-name">Branto Ceramic, LLC</span></div>
    <div class="entity-tag">A Voltline Assemblies, Inc. Company</div>
    <div class="entity-url">www.brantoceramic.example</div>
  </div>
  <div class="entity entity-omra">
    <div class="entity-head"><span class="entity-mark"></span><span class="entity-name">OMRA Metering Devices Corporation</span></div>
    <div class="entity-tag">A Voltline Assemblies, Inc. Company</div>
    <div class="entity-url">www.omra-kfsd.example</div>
  </div>
  <div class="entity entity-summit">
    <div class="entity-head"><span class="entity-mark"></span><span class="entity-name">Summit Breaker</span></div>
    <div class="entity-tag">A Voltline Assemblies, Inc. Company</div>
    <div class="entity-url">www.summitbreaker.example</div>
  </div>
</section>

</body>
</html>
```